Discount banner for dog articles

Banner size: 820 x 340.
Must make visitors want to buy.
The banner should be about DOG harness and accessories and discounts up to 70% until 1 November.
Must be editable. (prefferably in photoshop or corel)
You can use my images for products and add your own for the rest.
It is not mandatory to use all my images. Just get the idea across.
Website address: [login to view URL]

```html
<!DOCTYPE html>
<html lang="en">
<head>
<meta charset="UTF-8">
<title>Dog Harness and Accessories – Sale</title>
<link rel="stylesheet" href="https://fonts.googleapis.com/css2?family=Oswald:wght@500;600&family=Archivo+Black&display=swap">
<style>
  :root {
    --orange: #f26a10;
    --orange-deep: #e45a05;
    --ink: #141414;
    --bg-light: #f4f4f4;
    --bg-mid: #dcdcdc;
    --white: #ffffff;
    --fur-light: #e8b46a;
    --fur-mid: #c9863a;
    --fur-dark: #9a5a22;
  }
  html, body {
    margin: 0;
    padding: 0;
    overflow: hidden;
  }
  .banner {
    position: relative;
    width: 1200px;
    height: 498px;
    overflow: hidden;
    background: radial-gradient(ellipse at 65% 40%, var(--bg-light) 0%, #ececec 45%, var(--bg-mid) 100%);
    font-family: "Oswald", sans-serif;
  }
  .corner-swoosh {
    position: absolute;
    left: 0;
    top: 0;
  }
  .brand {
    position: absolute;
    left: 14px;
    top: 42px;
    display: flex;
    align-items: center;
    gap: 6px;
    font-family: "Oswald", sans-serif;
    font-weight: 600;
    font-size: 17px;
    letter-spacing: 0.5px;
    color: var(--orange-deep);
  }
  .brand-dot {
    width: 14px;
    height: 14px;
    border-radius: 50%;
    background: var(--orange-deep);
  }
  .puppy-photo {
    position: absolute;
    left: 140px;
    top: -10px;
    width: 570px;
    height: 420px;
    border-radius: 46% 46% 30% 30%;
    background: radial-gradient(ellipse at 50% 45%, var(--fur-light) 0%, var(--fur-mid) 55%, var(--fur-dark) 85%, rgba(154,90,34,0) 100%);
  }
  .discount-badge {
    position: absolute;
    left: 831px;
    top: 38px;
    width: 200px;
    height: 200px;
    border-radius: 50%;
    background: var(--orange);
    display: flex;
    flex-direction: column;
    align-items: center;
    justify-content: center;
    font-family: "Archivo Black", sans-serif;
    color: var(--white);
    text-align: center;
    line-height: 0.95;
    -webkit-text-stroke: 2px var(--ink);
    paint-order: stroke fill;
    text-shadow: 2px 2px 0 var(--ink);
  }
  .discount-badge .lead { font-size: 34px; }
  .discount-badge .amount { font-size: 64px; }
  .discount-badge .label { font-size: 32px; }
  .deadline {
    position: absolute;
    left: 765px;
    top: 290px;
    margin: 0;
    font-weight: 500;
    font-size: 40px;
    letter-spacing: 0.5px;
    color: var(--ink);
  }
  .bottom-bands {
    position: absolute;
    left: 0;
    top: 0;
  }
  .product-line {
    position: absolute;
    left: 0;
    width: 1200px;
    top: 412px;
    margin: 0;
    padding-right: 310px;
    box-sizing: border-box;
    text-align: right;
    font-weight: 500;
    font-size: 36px;
    color: var(--ink);
  }
</style>
</head>
<body>
<div class="banner">
  <svg class="corner-swoosh" width="200" height="230" viewBox="0 0 200 230" aria-hidden="true">
    <path d="M0,0 L165,0 Q150,170 0,210 Z" fill="var(--white)"/>
    <path d="M0,208 Q150,175 165,0" fill="none" stroke="var(--orange)" stroke-width="12"/>
  </svg>
  <div class="brand"><span class="brand-dot"></span>PAWLINE</div>

  <div class="puppy-photo" role="img" aria-label="Golden retriever puppy looking at the viewer"></div>

  <div class="discount-badge">
    <span class="lead">UP TO</span>
    <span class="amount">70%</span>
    <span class="label">DISCOUNTS</span>
  </div>

  <p class="deadline">UNTIL 1 NOVEMBER</p>

  <svg class="bottom-bands" width="1200" height="498" viewBox="0 0 1200 498" aria-hidden="true">
    <path d="M0,450 Q760,280 1200,440 L1200,498 L0,498 Z" fill="var(--ink)"/>
    <path d="M0,470 Q760,312 1200,462 L1200,498 L0,498 Z" fill="var(--orange)"/>
  </svg>

  <p class="product-line">DOG HARNESS AND ACCESSORIES</p>
</div>
</body>
</html>
```